Create a Magazine Ad for an Harborvale Claims

we need an 8 X 13 ad to be on the back of a magazine cover. We have the text Attached and want a similar look and feel to our website : www.harborvale-claims.example. The ad should be targeted to white males 55 years or older who are conservative and worked in industry or industrial plants. The main offer is a free case review and trying to get them to call the telephone number.

Target Market(s)

White collar men who worked in industrial plants. Age 55 years or older.

Industry/Entity Type

Legal

Requirements
Must have
• Pictures of white middle class conservative man or man and woman
Nice to have
• look at www.harborvale-claims.example to an. idea of what we are looking for

```html
<!DOCTYPE html>
<html lang="en">
<head>
<meta charset="utf-8">
<title>Mesothelioma Compensation Ad</title>
<link rel="stylesheet" href="https://fonts.googleapis.com/css2?family=Oswald:wght@500;700&family=Open+Sans:wght@400;600;700&display=swap">
<style>
  :root{
    --navy:#0f2f4f;
    --navy-deep:#0a233c;
    --yellow:#f6b91b;
    --orange:#f28c1a;
    --white:#ffffff;
    --ink:#1d2f44;
    --photo-warm-a:#c9b7a2;
    --photo-warm-b:#7e8ea0;
    --photo-man-a:#d9cfc3;
    --photo-man-b:#8f8476;
  }
  *{box-sizing:border-box;margin:0;padding:0}
  html,body{width:889px;height:1200px;overflow:hidden;background:var(--navy)}
  .ad{position:relative;width:889px;height:1200px;display:flex;flex-direction:column;background:var(--navy);font-family:"Open Sans",Arial,sans-serif;color:var(--white);overflow:hidden}

  /* Hero */
  .hero{position:relative;height:345px;flex:none}
  .hero-photo{position:absolute;left:450px;top:0;width:439px;height:320px;border-bottom-left-radius:180px;background:linear-gradient(135deg,var(--photo-warm-a),var(--photo-warm-b))}
  .hero-arc{position:absolute;left:440px;top:270px}
  .brand{position:absolute;left:40px;top:30px;display:flex;align-items:center;gap:12px}
  .brand-dot{width:22px;height:22px;border-radius:50%;background:var(--yellow)}
  .brand-name{font-family:"Oswald",Arial,sans-serif;font-weight:700;font-size:24px;letter-spacing:1px;text-transform:uppercase}
  .headline{position:absolute;left:40px;top:112px;width:400px;font-family:"Oswald",Arial,sans-serif;font-weight:700;font-size:44px;line-height:1.08;text-transform:uppercase}
  .headline .accent{color:var(--yellow)}

  /* Intro copy */
  .intro{flex:none;padding:0 40px 44px;width:610px;font-size:13.5px;line-height:1.4}
  .intro p + .ticks{margin-top:4px}
  .ticks{list-style:none;margin-bottom:10px}
  .ticks li{padding-left:22px;position:relative}
  .ticks li::before{content:"";position:absolute;left:2px;top:5px;width:11px;height:11px;border-radius:2px;background:var(--yellow)}
  .trust-title{margin-top:12px;font-family:"Oswald",Arial,sans-serif;font-weight:500;font-size:26px;line-height:1.1;color:var(--yellow)}
  .trust-copy{margin-top:6px;font-size:13px;line-height:1.4}

  /* Lower section */
  .lower{position:relative;flex:1;background:var(--white);color:var(--ink);padding:22px 40px 0}
  .wave{position:absolute;left:0;top:-38px}
  .man-photo{position:absolute;right:0;top:40px;bottom:0;width:290px;border-top-left-radius:140px;background:linear-gradient(160deg,var(--photo-man-a),var(--photo-man-b))}
  .lower-col{position:relative;width:530px}
  .money-title{font-family:"Oswald",Arial,sans-serif;font-weight:700;font-size:29px;line-height:1.1;color:var(--navy)}
  .money-copy{margin-top:6px;font-size:13px;line-height:1.4}

  .results{margin-top:12px;background:var(--navy);border-radius:8px;padding:10px;display:grid;grid-template-columns:repeat(3,1fr);gap:8px}
  .result{border:2px solid var(--yellow);border-radius:6px;padding:5px 4px;text-align:center;background:var(--navy-deep)}
  .result-amount{font-family:"Oswald",Arial,sans-serif;font-weight:700;font-size:17px;line-height:1.2;color:var(--yellow)}
  .result-note{font-size:10.5px;color:var(--white)}

  .eligible{margin-top:10px;font-family:"Oswald",Arial,sans-serif;font-weight:500;font-size:18px;color:var(--orange)}
  .cta-bar{display:inline-block;margin-top:4px;background:var(--navy);color:var(--yellow);font-weight:700;font-size:12px;padding:3px 14px;border-radius:3px;text-transform:uppercase}
  .phone{margin-top:2px;font-family:"Oswald",Arial,sans-serif;font-weight:700;font-size:38px;line-height:1.15;color:var(--navy);display:flex;align-items:center;gap:10px}
  .address{font-size:11px;color:var(--ink)}
</style>
</head>
<body>
<div class="ad">
  <header class="hero">
    <div class="hero-photo" role="img" aria-label="Photo of a smiling senior couple sitting together"></div>
    <svg class="hero-arc" width="449" height="80" viewBox="0 0 449 80" aria-hidden="true">
      <path d="M0 50 Q220 80 449 8" fill="none" stroke="var(--yellow)" stroke-width="12"/>
      <path d="M0 68 Q220 98 449 28" fill="none" stroke="var(--white)" stroke-width="4"/>
    </svg>
    <div class="brand"><span class="brand-dot"></span><span class="brand-name">Harborvale Claims</span></div>
    <h1 class="headline">Diagnosed with<br>Mesothelioma,<br><span class="accent">You could be owed<br>compensation</span></h1>
  </header>

  <section class="intro">
    <p><strong>It's very likely you developed this disease through asbestos exposure. Mesothelioma patients are getting multi-million dollar settlements, decades later, from:</strong></p>
    <ul class="ticks">
      <li>Exposure to asbestos products,</li>
      <li>An employer, or</li>
      <li>Talcum baby powder companies.</li>
    </ul>
    <p><strong>We can help you find out if you qualify for a case in minutes.</strong></p>
    <ul class="ticks">
      <li>We'll analyze your situation at no cost</li>
      <li>Determine how much compensation you could be entitled too</li>
      <li>Show you the next steps to get what you're owed</li>
    </ul>
    <h2 class="trust-title">$30 Billion is Available in<br>Trust for Mesothelioma Patients</h2>
    <p class="trust-copy">Tradesmen in many industries were negligently exposed to asbestos materials well into the 1980s. Whether you developed Mesothelioma yourself due to asbestos exposure or you're the surviving family of a lost loved one you could be entitled to significant compensation.</p>
  </section>

  <section class="lower">
    <svg class="wave" width="889" height="60" viewBox="0 0 889 60" aria-hidden="true">
      <path d="M0 30 Q380 -4 889 22 L889 60 L0 60 Z" fill="var(--white)"/>
      <path d="M0 30 Q380 -4 889 22" fill="none" stroke="var(--yellow)" stroke-width="6"/>
    </svg>
    <div class="man-photo" role="img" aria-label="Photo of a smiling older man in glasses"></div>

    <div class="lower-col">
      <h2 class="money-title">How much Money Can People<br>Receive from a Mesothelioma Case?</h2>
      <p class="money-copy">Depending on where you were exposed and a few other factors, you can get a settlement from 5 to 7 figures. Here are a few examples of Mesothelioma Settlements received by our clients. These figures are the total compensation after all attorney fees and expenses are deducted.</p>

      <div class="results">
        <div class="result"><div class="result-amount">$1,200,000</div><div class="result-note">Shipyard welder, Texas</div></div>
        <div class="result"><div class="result-amount">$950,000</div><div class="result-note">Refinery pipefitter</div></div>
        <div class="result"><div class="result-amount">$2,400,000</div><div class="result-note">Power plant electrician</div></div>
        <div class="result"><div class="result-amount">$780,000</div><div class="result-note">Navy boiler technician</div></div>
        <div class="result"><div class="result-amount">$1,650,000</div><div class="result-note">Chemical plant operator</div></div>
        <div class="result"><div class="result-amount">$3,100,000</div><div class="result-note">Steel mill mechanic</div></div>
      </div>

      <p class="eligible">Find out if you're Eligible for FREE in 5 Minutes.</p>
      <div class="cta-bar">Get your free evaluation now!</div>
      <div class="phone">
        <svg width="30" height="30" viewBox="0 0 24 24" aria-hidden="true"><path fill="var(--orange)" d="M6.6 10.8a15.1 15.1 0 0 0 6.6 6.6l2.2-2.2c.3-.3.7-.4 1-.2 1.1.4 2.3.6 3.6.6.6 0 1 .4 1 1V20c0 .6-.4 1-1 1C10.6 21 3 13.4 3 4c0-.6.4-1 1-1h3.5c.6 0 1 .4 1 1 0 1.3.2 2.5.6 3.6.1.3 0 .7-.2 1z"/></svg>
        CALL 1-555 0199
      </div>
      <p class="address">Marlow &amp; Teague, LLP, 1400 Quarry Lane, Houston, TX</p>
    </div>
  </section>
</div>
</body>
</html>
```